Regenerative Medicine Brochure

I want a clean modern bi-fold or tri-fold brochure. We offer non-surgical joint repair for knees, shoulders, and hips. We have many services available including regenerative medicine including stem cell allograft, palatelet rich plasma, prolotherapy, triggerpoint injection, chiropractic and rehab therapies. We are a modern multidisciplinary clinic in coastal California. My logo is already complete and is a vibrant green color. I prefer lots of white space with some areas for service description and what conditions may benefit from the services. Design should convey modern treatments, upscale office and practice, and our target audience is older adults who want to maintain an active pain-free lifestyle.

Target Market(s)

Sports injuries, athletes, seniors who are active, knee pain, shoulder pain, arthritis.

Industry/Entity Type

Alternative Medicine

Font styles to use
Serif

Colors
9bcb3c

Requirements
Must have
• Small white space where we can write date, time, location of next event/class. Colors in brochure to coordinate with logo colors provided.

```html
<!DOCTYPE html>
<html lang="en">
<head>
<meta charset="utf-8">
<title>Regenerative Medicine Brochure – Harborview Joint Care</title>
<link href="https://fonts.googleapis.com/css2?family=Merriweather:wght@400;700&family=Crimson+Text:wght@400;600&display=swap" rel="stylesheet">
<style>
  :root{
    --green:#9bcb3c;
    --ink:#2a2e33;
    --text:#3e4247;
    --white:#ffffff;
    --paper:#ffffff;
    --rule:#c9cdd1;
  }
  *{box-sizing:border-box;margin:0;padding:0}
  html,body{width:1200px;height:1200px;overflow:hidden;background:var(--paper)}
  body{position:relative;font-family:"Crimson Text",Georgia,serif;color:var(--text)}

  .spread{position:absolute;left:188px;width:746px;height:526px;background:var(--white);overflow:hidden}
  .spread--inside{top:53px}
  .spread--outside{top:621px}
  .panel{position:absolute;top:0;height:526px;overflow:hidden}
  .panel--one{left:0;width:246px}
  .panel--two{left:246px;width:250px}
  .panel--three{left:496px;width:250px}
  .panel--green{background:var(--green)}

  .heading{font-family:"Merriweather",Georgia,serif;font-weight:400;line-height:1.3}
  .heading--green{color:var(--green)}
  .heading--white{color:var(--white)}
  .heading--dark{color:var(--ink)}
  .body-copy{font-size:8px;line-height:1.45}
  .body-copy p+p{margin-top:9px}
  .body-copy--white{color:var(--white)}

  .photo{position:absolute}

  /* inside spread */
  .anatomy-visual{left:0;top:0;width:246px;height:246px;
    background:radial-gradient(circle at 50% 45%,#4c6bd8 0%,#1d3a8c 45%,#0b1a45 100%)}
  .what-heading{position:absolute;left:20px;top:260px;width:200px;font-size:14.5px}
  .what-copy{position:absolute;left:20px;top:302px;width:218px}

  .how-heading{position:absolute;left:15px;top:27px;width:225px;font-size:14px}
  .how-copy{position:absolute;left:15px;top:72px;width:216px}
  .runner-frame{position:absolute;left:-4px;top:354px;width:258px;height:258px;border-radius:50%;background:var(--white);padding:3px}
  .runner-visual{width:100%;height:100%;border-radius:50%;
    background:radial-gradient(circle at 45% 40%,#d9ecf7 0%,#9ccbe6 45%,#eef6fb 100%)}

  .areas-heading{position:absolute;left:10px;top:22px;width:230px;font-size:13.5px}
  .area-tile{position:absolute;width:102px;overflow:hidden}
  .area-tile .photo{position:static;width:100%;height:100%}
  .area-label{position:absolute;left:0;right:0;bottom:0;height:14px;background:var(--green);
    color:var(--white);font-family:"Merriweather",Georgia,serif;font-size:8.5px;text-align:center;line-height:14px}
  .tile-col-a{left:6px}
  .tile-col-b{left:117px}
  .tile-row-1{top:74px;height:82px}
  .tile-row-2{top:169px;height:69px}
  .tile-row-3{top:248px;height:85px}
  .area-photo{background:linear-gradient(150deg,#f3efec 0%,#d9c3b4 55%,#c65a4c 100%)}
  .area-photo--dark{background:linear-gradient(150deg,#2a2a2a 0%,#a77f6b 55%,#d84a3c 100%)}
  .areas-copy{position:absolute;left:10px;top:343px;width:210px}

  /* outside spread */
  .expect-heading{position:absolute;left:19px;top:27px;width:220px;font-size:18px;line-height:1.45}
  .expect-copy{position:absolute;left:19px;top:106px;width:214px}
  .cta{position:absolute;left:21px;top:419px;width:200px;font-size:12.5px;line-height:1.5}

  .knee-visual{left:0;top:0;width:250px;height:270px;
    background:radial-gradient(ellipse at 75% 30%,#c9a38c 0%,#e4cdbd 35%,rgba(255,255,255,0) 72%)}
  .event-line{position:absolute;height:1px;background:var(--rule)}
  .event-line--1{left:24px;top:194px;width:140px}
  .event-line--2{left:28px;top:242px;width:136px}
  .event-line--3{left:24px;top:288px;width:140px}
  .mark{position:absolute;left:30px;top:346px;width:190px;display:flex;align-items:center;justify-content:center;gap:8px}
  .mark-square{width:16px;height:16px;background:var(--green)}
  .mark-name{font-family:"Merriweather",Georgia,serif;font-weight:700;font-size:24px;color:var(--green)}
  .contact{position:absolute;left:10px;top:417px;width:230px;text-align:center;font-size:7.6px;line-height:2.1;color:var(--text)}
  .contact-key{color:var(--green)}

  .cover-shape{position:absolute;left:0;top:0}
  .cover-title{position:absolute;left:418px;top:19px;width:400px;text-align:center;color:var(--ink)}
  .cover-title__main{display:block;font-family:"Merriweather",Georgia,serif;font-weight:700;font-size:29px;line-height:1.2}
  .cover-title__sub{display:block;font-family:"Merriweather",Georgia,serif;font-weight:700;font-size:18px;line-height:1.3}
  .cover-intro{position:absolute;left:512px;top:80px;width:214px;text-align:center;color:var(--white);font-size:8.3px;line-height:1.55}
  .cover-ring{position:absolute;left:523px;top:200px;width:188px;height:188px;border-radius:50%;border:2px solid #d7ecb0;padding:3px}
  .cover-photo{width:100%;height:100%;border-radius:50%;border:4px solid var(--white);
    background:radial-gradient(circle at 50% 40%,#3a4a5c 0%,#7d8e97 45%,#c8d6cf 100%)}
  .cover-name{position:absolute;left:500px;top:412px;width:240px;text-align:center;
    font-family:"Merriweather",Georgia,serif;font-weight:400;font-size:17px;color:var(--ink);line-height:1.2}
</style>
</head>
<body>

<section class="spread spread--inside">
  <div class="panel panel--one">
    <div class="photo anatomy-visual" role="img" aria-label="Glowing anatomy illustration highlighting hand, shoulder, spine, ankle and knee joints"></div>
    <h2 class="heading heading--green what-heading">What is regenerative medicine?</h2>
    <div class="body-copy what-copy">
      <p>Regenerative medicine is a form of biotechnology that involves injecting regenerative medicine products into injured tissues to help your body repair damage. Regenerative medicine uses tissue engineering techniques to repair muscles, ligaments, cartilage, and tendons damaged by injuries, overuse, and osteoarthritis. The medical providers at Harborview Joint Care select from a variety of available treatments and products. These include amniotic allografts, hyaluronic acid, regenerative cells, and cytokines which are powerful growth factors that may help regenerate your own body's tissues.</p>
      <p>After you're injection with the amniotic allograft serum, the growth factors trigger repair at the site of injection. Over the course of the next several weeks, cells grow and multiply forming new tissue.</p>
    </div>
  </div>

  <div class="panel panel--two panel--green">
    <h2 class="heading heading--white how-heading">How does regenerative medicine work?</h2>
    <div class="body-copy body-copy--white how-copy">
      <p>The team uses lab-grade products that are sterilized and processed to inject into the injured area. Once injected, it is thought that these powerful products differentiate into a variety of tissues to trigger your own body to repair damaged tissues. This damage may involve minor tears in muscles, ligaments, and tendons, or cartilage and meniscus breakdown in joints.</p>
      <p>Regenerative medicine products contain the basic building blocks of the body tissues — including proteins, amino acids, and cytokines — responsible for healing and tissue growth. They also provide anti-inflammatory benefits by promoting repair of tissues affected by inflammation.</p>
      <p>While some inflammation is normal and has a benefit to healing injuries, long-term inflammation causes pain, swelling, and further damage to tissues. When you experience too much inflammation, it does more harm than good. Instead of constantly relying on anti-inflammatory medications, regenerative products may be able to correct the problem at the source and reduce the production of natural inflammatory chemicals so you can heal.</p>
    </div>
    <div class="runner-frame">
      <div class="runner-visual" role="img" aria-label="Translucent running figure with glowing joint pain points"></div>
    </div>
  </div>

  <div class="panel panel--three">
    <h2 class="heading heading--green areas-heading">Regenerative medicine may be used in the following areas:</h2>
    <div class="area-tile tile-col-a tile-row-1"><div class="photo area-photo" role="img" aria-label="Person holding a sore shoulder"></div><span class="area-label">Shoulder</span></div>
    <div class="area-tile tile-col-b tile-row-1"><div class="photo area-photo--dark" role="img" aria-label="Arm with highlighted elbow pain"></div><span class="area-label">Elbow</span></div>
    <div class="area-tile tile-col-a tile-row-2"><div class="photo area-photo" role="img" aria-label="Hand holding a painful wrist"></div><span class="area-label">Wrist</span></div>
    <div class="area-tile tile-col-b tile-row-2"><div class="photo area-photo" role="img" aria-label="Person holding lower back and hip"></div><span class="area-label">Hip</span></div>
    <div class="area-tile tile-col-a tile-row-3"><div class="photo area-photo--dark" role="img" aria-label="Hands holding a painful knee"></div><span class="area-label">Knee</span></div>
    <div class="area-tile tile-col-b tile-row-3"><div class="photo area-photo" role="img" aria-label="Foot with highlighted ankle pain"></div><span class="area-label">Ankle</span></div>
    <div class="body-copy areas-copy">
      <p>There are many additional types of bone and soft tissue problems, including arthritis, that these injections may benefit.</p>
      <p>With regenerative medicine and amniotic allograft treatments, the team supports the natural healing abilities of your body without the need for drugs or surgical repair and painful recovery. However, not all forms of regenerative medicine are equal. At Harborview Joint Care, the team only works with the best regenerative medicine labs to ensure that the right kind of products are selected and that they are of the best quality and highest safety.</p>
    </div>
  </div>
</section>

<section class="spread spread--outside">
  <div class="panel panel--one">
    <h2 class="heading heading--dark expect-heading">What can I expect from regenerative medicine treatments?</h2>
    <div class="body-copy expect-copy">
      <p>During your visit, the team begins with a consultation and physical exam to determine if you're a candidate for regenerative medicine. They ask about your symptoms, condition, overall health, and lifestyle. If you're a candidate, the team then explains the procedure and what to expect both during and afterward.</p>
      <p>For the procedure, the team first cleans your skin and applies a topical numbing cream to your skin, if needed. Next, the team injects regenerative products into the treatment area. You may feel a slight pinch or burning sensation during the injection. The injection takes less than five minutes and you can return to your usual activities the same day. Mild soreness at the injection site is possible for two to three days.</p>
      <p>Over the coming weeks and months, the injected products help repair damaged tissues at the treatment site. Most people notice results after two months. Follow-up care may be recommended based on your condition and initial results. The team has seen dramatic results with regenerative medicine treatments, however, individual results can vary. Speak to the team to see if regenerative medicine is right for you.</p>
    </div>
    <p class="heading heading--green cta">To learn more, schedule a visit online or by phone at Harborview Joint Care now.</p>
  </div>

  <div class="panel panel--two">
    <div class="photo knee-visual" role="img" aria-label="Active adult holding a sore knee, fading into white"></div>
    <div class="event-line event-line--1"></div>
    <div class="event-line event-line--2"></div>
    <div class="event-line event-line--3"></div>
    <div class="mark"><span class="mark-square"></span><span class="mark-name">HJC</span></div>
    <div class="contact">
      <div><span class="contact-key">Adress:</span> 14 Tideway Lane, Bayfield</div>
      <div><span class="contact-key">Phone:</span> (555) 010 2040</div>
      <div><span class="contact-key">Email:</span> hello@harborviewjoint.example</div>
      <div><span class="contact-key">web:</span> www.harborviewjoint.example</div>
    </div>
  </div>

  <svg class="cover-shape" width="746" height="526" viewBox="0 0 746 526" aria-hidden="true">
    <path d="M440 0 L746 0 L746 311 C 660 385 470 335 418 230 C 388 150 400 60 440 0 Z" fill="#9bcb3c"/>
  </svg>
  <h1 class="cover-title">
    <span class="cover-title__main">Regenerative</span>
    <span class="cover-title__sub">Medicine Q &amp; A</span>
  </h1>
  <p class="cover-intro">For joint arthritis and muscle pain and injuries, the team at Harborview Joint Care offers minimally invasive regenerative medicine techniques to help you recover from chronic pain. Located in Bayfield, California, the medical team utilizes advanced restorative techniques to support the natural healing of injured joints and soft tissues without the need for surgery. To learn more, schedule a consultation online or by phone today.</p>
  <div class="cover-ring">
    <div class="cover-photo" role="img" aria-label="Woman seen from behind holding her lower back"></div>
  </div>
  <p class="cover-name">Harborview Joint Care</p>
</section>

</body>
</html>
```